Design a web site for my business - Finish Craft Coralbay.

We are a family business that handles design, fabrication and installation of powder coated aluminum, stainless steel and glass products. Including handrails, privacy slat screens, electric gates and pool fencing. We are based in the Whitsundays in North Queensland and service an area from Airlie Beach to Townsville.

Target Market(s)

Domestic and commercial

Industry/Entity Type

fabrication - manufacturing

Coding

Coded - Design and coding required

Number of Pages Required

5+ page

Colors
0054AA
0677BA
7BADD7
CADEEF
E8F1F8

Requirements
Must have
• photo galleries, contact page, one page for privacy screens, balustrades, glass fencing, stainless steel handrail, powder coated aluminium handrails and pool fencing

```html
<!DOCTYPE html>
<html lang="en">
<head>
<meta charset="utf-8">
<title>Finish Craft Coralbay — Architectural Metal &amp; Glass</title>
<link href="https://fonts.googleapis.com/css2?family=Montserrat:wght@500;600;700&family=Inter:wght@400;500;600&display=swap" rel="stylesheet">
<style>
:root{
  --blue:#0054AA;
  --blue-mid:#0677BA;
  --blue-soft:#7BADD7;
  --blue-pale:#CADEEF;
  --blue-mist:#E8F1F8;
  --ink:#1b2226;
  --ink-2:#232a2f;
  --text:#4a5560;
  --muted:#8a949c;
  --line:#e3e7ea;
  --white:#ffffff;
}
*{box-sizing:border-box;margin:0;padding:0}
html,body{width:1200px;height:4482px;overflow:hidden}
body{font-family:"Inter",sans-serif;color:var(--ink);background:var(--white);position:relative}
h1,h2,h3,.brand{font-family:"Montserrat",sans-serif}
a{text-decoration:none;color:inherit}

/* nav */
.nav{position:absolute;top:0;left:0;width:1200px;height:76px;background:rgba(232,241,248,.92);display:flex;align-items:center;padding:0 61px;z-index:5}
.brand{font-weight:700;font-size:21px;letter-spacing:-.3px;color:var(--ink)}
.nav-links{margin-left:auto;display:flex;align-items:center;gap:37px;font-size:13px;font-weight:500;color:#555}
.nav-links .active{color:var(--blue);font-weight:600;border-bottom:2px solid var(--blue);padding-bottom:6px;margin-top:8px}
.btn-dark{background:var(--ink);color:#fff;font-weight:600;font-size:13px;border-radius:5px;padding:12px 22px}

/* hero */
.hero{position:absolute;top:76px;left:0;width:1200px;height:1044px;overflow:hidden}
.hero-photo{position:absolute;inset:0;background:
  linear-gradient(90deg,rgba(240,245,248,.95) 0%,rgba(240,245,248,.8) 30%,rgba(240,245,248,.1) 60%,rgba(240,245,248,0) 100%),
  linear-gradient(180deg,#bcd7ea 0%,#dfe9ee 30%,#b9c8cc 48%,#7fc3d4 62%,#9fd4df 80%,#d6e5e8 100%)}
.hero-inner{position:absolute;left:61px;top:316px;width:560px}
.tag{display:inline-block;background:var(--blue-pale);color:var(--blue);font-size:12px;font-weight:600;padding:5px 14px;border-radius:12px}
.hero h1{font-size:61px;line-height:66px;font-weight:700;letter-spacing:-1px;margin-top:26px}
.hero h1 span{color:var(--blue)}
.hero p{font-size:16px;line-height:27px;color:var(--text);margin-top:26px;width:480px}
.hero-actions{display:flex;gap:16px;margin-top:38px}
.hero-actions a{height:59px;display:flex;align-items:center;gap:12px;font-size:13px;font-weight:600;border-radius:5px;padding:0 37px}
.btn-primary{background:var(--ink);color:#fff;width:219px}
.btn-ghost{background:rgba(240,242,240,.85);color:var(--ink);width:170px}
.scroll{position:absolute;left:0;right:0;top:964px;text-align:center;font-size:11px;letter-spacing:1.5px;color:#444}

/* process */
.process{position:absolute;top:1120px;left:0;width:1200px;height:784px;background:#f6f7f8;text-align:center}
.process h2{font-size:46px;font-weight:600;margin-top:122px;letter-spacing:-.5px}
.process .lead{font-size:16px;line-height:27px;color:var(--text);margin:22px auto 0;width:620px}
.steps{position:absolute;top:317px;left:61px;display:flex;gap:23px;text-align:left}
.step{width:343px;height:325px;background:#fff;border:1px solid var(--line);border-radius:8px;padding:36px 36px 0;box-shadow:0 4px 14px rgba(0,0,0,.03)}
.step:nth-child(2){height:346px}
.step-icon{width:59px;height:59px;border-radius:6px;background:var(--blue);display:flex;align-items:center;justify-content:center}
.step:nth-child(2) .step-icon{background:var(--ink-2)}
.step h3{font-size:22px;font-weight:600;margin-top:31px}
.step p{font-size:14px;line-height:22.5px;color:var(--text);margin-top:20px}

/* products */
.products{position:absolute;top:1904px;left:0;width:1200px;height:1319px;background:var(--blue-mist)}
.products h2{position:absolute;left:61px;top:120px;font-size:46px;font-weight:600;letter-spacing:-.5px}
.products .lead{position:absolute;left:61px;top:192px;width:540px;font-size:16px;line-height:27px;color:var(--text)}
.catalog{position:absolute;right:61px;top:250px;font-size:14px;font-weight:600;color:var(--blue)}
.card{position:absolute;border-radius:6px;overflow:hidden;color:#fff}
.card .photo{position:absolute;inset:0}
.card .shade{position:absolute;inset:0;background:linear-gradient(180deg,rgba(0,0,0,0) 40%,rgba(0,0,0,.6) 100%)}
.card .body{position:absolute;left:37px;bottom:37px}
.card h3{font-size:29px;font-weight:500}
.card p{font-size:14px;line-height:22px;margin-top:8px;opacity:.85;width:400px}
.card .pill{display:inline-block;background:#fff;color:var(--ink);font-size:13px;font-weight:600;border-radius:4px;padding:10px 22px;margin-top:16px}
.card .link{display:inline-block;font-size:13px;font-weight:600;border-bottom:1px solid #fff;margin-top:12px;padding-bottom:2px}
.c-glass{left:61px;top:329px;width:708px;height:467px}
.c-glass .photo{background:linear-gradient(180deg,#8fb8cc 0%,#d4dcd6 30%,#5a7a55 55%,#2f6a7a 75%,#1f4e5a 100%)}
.c-hand{left:798px;top:329px;width:340px;height:467px}
.c-hand .photo{background:linear-gradient(135deg,#a9a8a4 0%,#8f8e8a 45%,#5b5a57 75%,#2e2d2b 100%)}
.c-hand h3{font-size:23px;line-height:30px}
.c-slat{left:61px;top:827px;width:339px;height:372px}
.c-slat .photo{background:linear-gradient(180deg,#c8ccce 0%,#8d9398 40%,#6b6e6f 70%,#4a4a46 100%)}
.c-slat h3{font-size:23px}
.c-slat .body{left:30px;bottom:30px}
.c-gate{left:430px;top:827px;width:708px;height:372px}
.c-gate .photo{background:linear-gradient(180deg,#eef0f2 0%,#2c3a4e 25%,#222b38 60%,#4b4f55 100%)}
.c-gate .body{left:30px;bottom:30px}

/* cta */
.cta{position:absolute;top:3223px;left:0;width:1200px;height:760px;background:var(--ink)}
.cta-panel{position:absolute;left:61px;top:90px;width:1077px;height:578px;background:var(--ink-2);border-radius:20px}
.cta-copy{position:absolute;left:75px;top:145px;width:460px;color:#fff}
.cta-copy h2{font-size:46px;line-height:55px;font-weight:700}
.cta-copy p{font-size:16px;line-height:27px;color:#9aa3aa;margin-top:30px}
.trust{display:flex;align-items:center;margin-top:38px;gap:22px;font-size:13px;font-weight:600}
.avatars{display:flex}
.avatars span{width:40px;height:40px;border-radius:50%;border:2px solid var(--ink-2);display:flex;align-items:center;justify-content:center;font-size:14px;font-weight:600;margin-right:-10px}
.avatars span:nth-child(1){background:#eef0f2;color:var(--ink)}
.avatars span:nth-child(2){background:var(--blue);color:#fff}
.avatars span:nth-child(3){background:#6c757c;color:#fff}
.form{position:absolute;left:562px;top:75px;width:440px;height:430px;background:#fff;border-radius:10px;padding:36px 37px}
.form label{display:block;font-size:13px;font-weight:600;margin-bottom:10px}
.row{display:flex;gap:15px}
.row > div{flex:1}
.field{height:44px;border:1px solid #d9dee2;border-radius:4px;padding:0 13px;display:flex;align-items:center;font-size:14px;color:#8b949b}
.field.select{color:var(--ink);justify-content:space-between}
.field.area{height:90px;align-items:flex-start;padding-top:14px}
.group{margin-top:20px}
.send{margin-top:22px;height:52px;border-radius:6px;background:var(--blue);color:#fff;font-size:14px;font-weight:600;display:flex;align-items:center;justify-content:center}

/* footer */
.footer{position:absolute;top:3983px;left:0;width:1200px;height:499px;background:var(--ink);border-top:1px solid #3a4248;color:#fff}
.fcol{position:absolute;top:75px}
.fcol h4{font-size:13px;letter-spacing:1.5px;font-weight:600}
.fcol ul{list-style:none;margin-top:30px}
.fcol li{font-size:11px;color:#8b949b;margin-bottom:25px}
.f-brand{left:61px;top:84px;width:220px}
.f-brand .brand{font-size:21px;line-height:31px;font-weight:600;color:#fff}
.f-brand p{font-size:14px;line-height:24px;color:#8b949b;margin-top:26px}
.socials{display:flex;gap:20px;margin-top:40px}
.socials span{width:34px;height:34px;border-radius:50%;background:#2c3439}
.f-contact p{font-size:15px;line-height:29px;color:#8b949b}
.f-contact p.first{margin-top:25px}
.f-contact .phone{color:var(--blue-soft);font-weight:600}
.copy{position:absolute;left:61px;top:457px;font-size:10px;color:#6f787f}
</style>
</head>
<body>

<header class="nav">
  <div class="brand">FINISH CRAFT CORALBAY</div>
  <nav class="nav-links">
    <a class="active" href="#">Home</a>
    <a href="#">Products</a>
    <a href="#">Process</a>
    <a href="#">Projects</a>
    <a class="btn-dark" href="#">Request a Quote</a>
  </nav>
</header>

<section class="hero">
  <div class="hero-photo" role="img" aria-label="Luxury coastal home with infinity pool and frameless glass pool fencing"></div>
  <div class="hero-inner">
    <span class="tag">Architectural Metal &amp; Glass</span>
    <h1>Engineered for the<br><span>Whitsunday Coast.</span></h1>
    <p>Providing premium glass pool fencing, balustrades, and custom fabrication services that combine industrial strength with luxury coastal aesthetics.</p>
    <div class="hero-actions">
      <a class="btn-primary" href="#">Request a Quote
        <svg width="16" height="14" viewBox="0 0 16 14"><path d="M1 7h13M9 2l5 5-5 5" fill="none" stroke="#fff" stroke-width="2"/></svg></a>
      <a class="btn-ghost" href="#">View Projects</a>
    </div>
  </div>
  <div class="scroll">SCROLL<br>
    <svg width="14" height="10" viewBox="0 0 14 10"><path d="M2 2l5 5 5-5" fill="none" stroke="#444" stroke-width="2"/></svg>
  </div>
</section>

<section class="process">
  <h2>The Fabrication Process</h2>
  <p class="lead">From initial concept to final installation, we deliver precision-engineered solutions tailored to the unique demands of the Whitsunday environment.</p>
  <div class="steps">
    <article class="step">
      <div class="step-icon"><svg width="22" height="24" viewBox="0 0 22 24"><circle cx="11" cy="4" r="2.5" fill="none" stroke="#fff" stroke-width="2"/><path d="M10 6L4 22M12 6l6 16M7 15h8" fill="none" stroke="#fff" stroke-width="2"/></svg></div>
      <h3>01. Design</h3>
      <p>We work with your architectural plans or site measurements to create 3D models and detailed shop drawings, ensuring perfect integration with your property.</p>
    </article>
    <article class="step">
      <div class="step-icon"><svg width="24" height="24" viewBox="0 0 24 24"><path d="M4 21h12M8 21v-4l-3-8 6-3 6 3M11 6V3" fill="none" stroke="#fff" stroke-width="2"/><circle cx="17" cy="9" r="2" fill="#fff"/></svg></div>
      <h3>02. Fabricate</h3>
      <p>Using marine-grade 316 stainless steel and toughened glass, our expert<br>welders and technicians craft your elements in our local Whitsunday facility.</p>
    </article>
    <article class="step">
      <div class="step-icon"><svg width="24" height="24" viewBox="0 0 24 24"><path d="M4 20L14 10M15 4l5 5-3 3-5-5zM20 20L10 10M4 4l3 3" fill="none" stroke="#fff" stroke-width="2.2"/></svg></div>
      <h3>03. Install</h3>
      <p>Our site team manages the entire installation process, ensuring structural integrity, safety compliance, and a flawless premium finish.</p>
    </article>
  </div>
</section>

<section class="products">
  <h2>Signature Products</h2>
  <p class="lead">Engineered for durability, designed for the view. Our products are built to withstand tropical conditions without compromising on aesthetic appeal.</p>
  <a class="catalog" href="#">Browse Full Catalog
    <svg width="18" height="10" viewBox="0 0 18 10"><path d="M0 5h16M12 1l4 4-4 4" fill="none" stroke="#0054AA" stroke-width="1.8"/></svg></a>

  <article class="card c-glass">
    <div class="photo" role="img" aria-label="Tropical home courtyard with pool enclosed by frameless glass fencing"></div>
    <div class="shade"></div>
    <div class="body">
      <h3>Glass Pool Fencing</h3>
      <p>Frameless and semi-frameless solutions that provide safety while maintaining an unobstructed view of the horizon.</p>
      <a class="pill" href="#">Explore Glass Fencing</a>
    </div>
  </article>

  <article class="card c-hand">
    <div class="photo" role="img" aria-label="Close-up of a brushed stainless steel handrail against concrete"></div>
    <div class="shade"></div>
    <div class="body">
      <h3>Handrails &amp;<br>Balustrades</h3>
      <a class="link" href="#">Learn More</a>
    </div>
  </article>

  <article class="card c-slat">
    <div class="photo" role="img" aria-label="Modern home facade with aluminium privacy slat screens"></div>
    <div class="shade"></div>
    <div class="body">
      <h3>Slat Screens</h3>
      <a class="link" href="#">Learn More</a>
    </div>
  </article>

  <article class="card c-gate">
    <div class="photo" role="img" aria-label="Decorative automated driveway gates lit at dusk"></div>
    <div class="shade"></div>
    <div class="body">
      <h3>Electric Gates</h3>
      <p>Custom sliding and swing gate systems with integrated automation and security features.</p>
      <a class="pill" href="#">View Gate Systems</a>
    </div>
  </article>
</section>

<section class="cta">
  <div class="cta-panel">
    <div class="cta-copy">
      <h2>Ready to start<br>your project?</h2>
      <p>Contact us today for a free on-site measure and quote. We service Airlie Beach, Proserpine, Bowen, and the greater Whitsunday region.</p>
      <div class="trust">
        <div class="avatars"><span>W</span><span>M</span><span>G</span></div>
        <span>Trusted by 500+ local homeowners</span>
      </div>
    </div>
    <form class="form">
      <div class="row">
        <div><label>Name</label><div class="field">John Smith</div></div>
        <div><label>Phone</label><div class="field">0400 000 000</div></div>
      </div>
      <div class="group"><label>Service Required</label>
        <div class="field select">Glass Pool Fencing
          <svg width="12" height="8" viewBox="0 0 12 8"><path d="M2 2l4 4 4-4" fill="none" stroke="#555" stroke-width="1.5"/></svg></div>
      </div>
      <div class="group"><label>Message</label><div class="field area">Tell us about your project...</div></div>
      <div class="send">Send Quote Request</div>
    </form>
  </div>
</section>

<footer class="footer">
  <div class="fcol f-brand">
    <div class="brand">FINISH CRAFT<br>CORALBAY</div>
    <p>The Whitsundays' leading specialist in architectural metalwork and premium glass solutions. Australian made for Australian conditions.</p>
    <div class="socials"><span></span><span></span></div>
  </div>
  <div class="fcol" style="left:336px">
    <h4>SERVICES</h4>
    <ul><li>Handrails</li><li>Slat Screens</li><li>Electric Gates</li><li>Pool Fencing</li></ul>
  </div>
  <div class="fcol" style="left:610px">
    <h4>SERVICE AREAS</h4>
    <ul><li>Airlie Beach</li><li>Townsville</li><li>Proserpine</li><li>Bowen</li></ul>
  </div>
  <div class="fcol f-contact" style="left:885px">
    <h4>CONTACT</h4>
    <p class="first">18 Harbour Rise,<br>Cannonvale QLD 4802</p>
    <p class="phone">PH: (07) 4900 1234</p>
    <p style="line-height:16px">hello@finishcraftcoralbay.com.au</p>
  </div>
  <div class="copy">© 2024 Finish Craft Coralbay. All Rights Reserved. Australian Made.</div>
</footer>

</body>
</html>
```